Modern Design for Norwegian Souvenir Playing Cards

We are looking for a design to place on the back of our new playing cards.

Target audience: Tourists in Norway
Dimensions: Standard poker card size, 88.0x63.5mm
Design: Modern - which may include traditional Norwegian elements. We want a premium design that communicates good quality. The design should be something that people associate with Norway, in some way. We would prefer it not to be seasonal, since we are going to sell it all year around.

Our company, Velmora Design AS, is a new, small company based in Norway. We specialize in making souvenirs with a twist. Now we take aim at conquering the playing card market with decks which have our own unique twist on the front side of each card. On the back side we want a design that continues our brand of modern look and premium quality. We are thinking a clean, minimalistic look that doesn't clutter the card and is instantly appealing in a store setting. These are preliminary thoughts, but we are open for other suggestions.

Target Market(s)

Tourists in Norway. Souvenir shops.

Industry/Entity Type

Store

Requirements
Must have
• Modern design.
• Premium/luxurious design.
• Something you associate with Norway, in some way.
Nice to have
• Norwegian elements of some sort (aka mountains, fjords, flag, colors of flag, map of Norway, etc.)
• Minimalistic design.
Should not have
• A design that is seasonal.
• Norwegian elements that is only associated with one particular place in Norway (like a famous building).

```html
<!DOCTYPE html>
<html lang="no">
<head>
<meta charset="utf-8">
<title>Norge – spillkort bakside</title>
<link rel="stylesheet" href="https://fonts.googleapis.com/css2?family=Open+Sans:wght@700&display=swap">
<style>
  :root {
    --flag-red: #c8102e;
    --flag-red-deep: #8f0b1f;
    --flag-red-light: #e23a4c;
    --flag-white: #ffffff;
    --flag-navy: #0b2a63;
  }
  html, body {
    margin: 0;
    padding: 0;
    overflow: hidden;
    background: var(--flag-white);
  }
  .card-back {
    position: relative;
    width: 867px;
    height: 1200px;
    overflow: hidden;
    background: var(--flag-white);
  }
  .flag-field {
    position: absolute;
    inset: 0;
    background:
      radial-gradient(ellipse at 30% 20%, var(--flag-red-light) 0%, transparent 55%),
      radial-gradient(ellipse at 75% 80%, var(--flag-red-light) 0%, transparent 50%),
      linear-gradient(160deg, var(--flag-red) 0%, var(--flag-red-deep) 100%);
  }
  .cross {
    position: absolute;
    inset: 0;
  }
  .wordmark {
    position: absolute;
    left: 34px;
    top: 468px;
    margin: 0;
    font-family: "Open Sans", Arial, sans-serif;
    font-weight: 700;
    font-size: 104px;
    line-height: 1;
    letter-spacing: 1px;
    color: var(--flag-white);
  }
</style>
</head>
<body>
  <main class="card-back">
    <div class="flag-field" role="img" aria-label="Pattern of many small waving Norwegian flags in red, white and blue"></div>

    <svg class="cross" width="867" height="1200" viewBox="0 0 867 1200" aria-hidden="true">
      <g class="cross-border" fill="var(--flag-white)">
        <rect x="343" y="0" width="200" height="1200"/>
        <rect x="0" y="398" width="867" height="280"/>
      </g>
      <g class="cross-centre" fill="var(--flag-navy)">
        <rect x="370" y="0" width="146" height="1200"/>
        <rect x="0" y="425" width="867" height="226"/>
      </g>
    </svg>

    <h1 class="wordmark">norge</h1>
  </main>
</body>
</html>
```